Nutrition product information web site

Nutrition Website (see upload) without Shop function but link to Velmora ASIN number that customer could order from Velmora direct. Content must be easily editable without coding. Web environment must be responsive to support mobile devices as well. design should be modern and clear. loading of web elements must be fast. not too much time consuming features.

Industry/Entity Type

Nutrition

Number of Pages Required

5+ page

Font styles to use
Sans Serif

Colors
33b8a4
9bcb3c
0255a3
0a90cc
a54499

Requirements
Must have
• read attached document
Nice to have
• read attached document
Should not have
• read attached document

```html
<!DOCTYPE html>
<html lang="en">
<head>
<meta charset="utf-8">
<title>Solvia – Nutrition</title>
<link href="https://fonts.googleapis.com/css2?family=Montserrat:wght@500&family=Noto+Serif:wght@400;700&family=Raleway:wght@400;500;700&display=swap" rel="stylesheet">
<style>
  :root{
    --teal:#1cb5bd;
    --teal-band:#35b6a0;
    --ink:#111;
    --body:#222;
    --muted:#777;
    --panel:#f4f4f4;
    --footer:#f2f2f2;
    --white:#fff;
  }
  *{box-sizing:border-box;margin:0;padding:0}
  html,body{width:1200px;height:2192px;overflow:hidden;background:var(--white)}
  body{position:relative;font-family:"Raleway",sans-serif;color:var(--body)}
  .abs{position:absolute}

  /* header */
  .social{display:flex;gap:14px}
  .social span{width:13px;height:13px;border-radius:50%;background:var(--ink);display:block}
  .header-social{left:152px;top:26px}
  .brand{display:flex;align-items:center;gap:12px;font-family:"Raleway",sans-serif;font-weight:700;color:var(--ink);letter-spacing:6px}
  .brand .mark{border:4px solid var(--teal);border-radius:50%;display:block}
  .header-brand{left:0;width:1200px;top:52px;justify-content:center;font-size:34px}
  .header-brand .mark{width:44px;height:44px}
  .main-nav{top:22px;font-family:"Noto Serif",serif;font-size:14.5px;color:var(--ink)}
  .main-nav a{position:absolute;white-space:nowrap;color:inherit;text-decoration:none}
  .main-nav a.active{color:var(--teal)}
  .main-nav .caret{font-size:10px;color:var(--teal);margin-left:4px}

  /* hero */
  .hero{left:0;top:172px;width:1200px;height:383px;
    background:linear-gradient(180deg,#7d8580 0%,#6f7d68 35%,#56683f 55%,#6b7578 75%,#4d5560 100%)}
  .hero-title{left:0;width:1200px;top:200px;text-align:center;font-family:"Montserrat",sans-serif;font-weight:500;font-size:35px;line-height:47px;color:var(--white)}
  .hero-product{left:611px;top:355px;width:180px;height:200px;background:linear-gradient(160deg,#ffffff,#e7e7e7)}
  .order-btn{left:791px;top:509px;width:311px;height:46px;background:var(--teal);color:var(--white);font-size:20px;display:flex;align-items:center;justify-content:center}

  /* intro */
  .intro-title{left:96px;top:646px;font-family:"Noto Serif",serif;font-weight:400;font-size:27px;color:var(--teal)}
  .intro-text{left:98px;top:702px;width:509px;font-size:16px;line-height:32px;text-align:justify;color:var(--ink)}
  .intro-product{left:723px;top:636px;width:300px;height:256px;border-radius:20px;
    background:radial-gradient(ellipse at 35% 55%,#d9cde3 0%,#eae6ee 40%,#ffffff 72%)}

  /* features */
  .feature{width:240px;text-align:center}
  .feature .icon{width:80px;height:66px;margin:0 auto;border-radius:50%}
  .feature h3{margin-top:22px;font-family:"Noto Serif",serif;font-weight:400;font-size:20px;color:var(--teal)}
  .feature p{margin-top:18px;font-size:17px;line-height:23px;color:var(--muted)}

  /* accordion */
  .acc{left:94px;width:1008px;height:42px;background:var(--panel);font-family:"Noto Serif",serif;font-size:17px;color:var(--ink);display:flex;align-items:center;justify-content:space-between;padding:0 18px 0 16px}
  .acc svg{display:block}
  .panel-title{left:0;width:1200px;top:1336px;text-align:center;font-family:"Noto Serif",serif;font-weight:400;font-size:20px;color:var(--teal)}
  .panel-rule{left:458px;top:1364px;width:254px;height:1.5px;background:var(--ink)}
  .panel-text{left:102px;top:1386px;width:538px;font-size:15px;line-height:31px;text-align:justify;color:var(--ink)}
  .panel-list{left:728px;top:1391px;list-style:none;font-size:15px;color:var(--ink)}
  .panel-list li{height:34px;display:flex;gap:26px}
  .panel-list li::before{content:"•";font-size:12px;line-height:20px}

  /* footer */
  .footer{left:0;top:1896px;width:1200px;height:296px;background:var(--footer)}
  .footer-brand{left:0;width:1200px;top:1960px;justify-content:center;font-size:40px}
  .footer-brand .mark{width:50px;height:50px}
  .footer-social{left:0;width:1200px;top:2071px;justify-content:center}
  .footer-nav{left:0;top:2108px;width:1200px;height:41px;background:var(--teal-band);font-family:"Noto Serif",serif;font-size:14.5px;color:var(--white)}
  .footer-nav a{position:absolute;top:11px;color:inherit;text-decoration:none;white-space:nowrap}
  .copyright{left:0;width:1200px;top:2160px;text-align:center;font-size:17px;color:#666}
</style>
</head>
<body>

<header>
  <div class="abs social header-social"><span aria-label="Social link"></span><span aria-label="Social link"></span><span aria-label="Social link"></span></div>
  <div class="abs brand header-brand"><span class="mark"></span>SOLVIA</div>
  <nav class="abs main-nav">
    <a class="active" style="left:729px">Home</a>
    <a style="left:797px">About Us</a>
    <a style="left:886px">Blog<span class="caret">⌄</span></a>
    <a style="left:944px">Products</a>
    <a style="left:1032px">Contact Us</a>
  </nav>
</header>

<section>
  <div class="abs hero" role="img" aria-label="Woman doing yoga beside a lake with forest"></div>
  <h1 class="abs hero-title">LOREM IPSUM DOLOR SIT AMET,<br>CONSECTETUR ELIT.</h1>
  <div class="abs hero-product" role="img" aria-label="White supplement sachet"></div>
  <a class="abs order-btn">Place Your Order at Velmora</a>
</section>

<section>
  <h2 class="abs intro-title">Praesent tempus turpis ?</h2>
  <p class="abs intro-text">Lorem Ipsum is simply dummy text of the printing and typesetting industry. Lorem Ipsum has been the industry's standard dummy text ever since the 1500s, when an unknown printer took a galley of type and scrambled it to make a type specimen book. It has survived not only five centuries,</p>
  <div class="abs intro-product" role="img" aria-label="Two supplement canisters, beauty and brain formulas"></div>
</section>

<section>
  <div class="abs feature" style="left:76px;top:965px"><div class="icon" role="img" aria-label="Green fern leaf" style="background:#7fb56a"></div><h3>LOREUM IPSUM</h3><p>Lorem Ipsum is simply dummy text of the printing and typesetting industry.</p></div>
  <div class="abs feature" style="left:351px;top:965px"><div class="icon" role="img" aria-label="Bunch of green grapes" style="background:#a9c66b"></div><h3>LOREUM IPSUM</h3><p>Lorem Ipsum is simply dummy text of the printing industry.</p></div>
  <div class="abs feature" style="left:611px;top:965px"><div class="icon" role="img" aria-label="Halved papaya" style="background:#f07a22"></div><h3>LOREUM IPSUM</h3><p>Lorem Ipsum is simply dummy text of the printing since the 1500s.</p></div>
  <div class="abs feature" style="left:881px;top:965px"><div class="icon" role="img" aria-label="Carrot with leaves" style="background:#f08a2c"></div><h3>LOREUM IPSUM</h3><p>Lorem Ipsum is simply dummy text of the printing since the 1500s.</p></div>
</section>

<section>
  <div class="abs acc" style="top:1266px">The Power Fruit for your health<svg width="12" height="12" viewBox="0 0 12 12"><rect x="0" y="5" width="12" height="2.2" fill="#111"/></svg></div>
  <h2 class="abs panel-title">THE POWER FRUIT FOR YOUR HEALTH</h2>
  <div class="abs panel-rule"></div>
  <p class="abs panel-text">Lorem Ipsum is simply dummy text of the printing and typesetting industry. Lorem Ipsum has been the industry's standard dummy text ever since the 1500s, when an unknown printer took a galley of type and scrambled it to make a type specimen book. It has survived not only five centuries, but also the leap into electronic typesetting, remaining essentially unchanged.</p>
  <ul class="abs panel-list">
    <li>Lorem Ipsum is simply dummy text of the printing</li>
    <li>Lorem Ipsum is simply dummy text of the printing</li>
    <li>Lorem Ipsum is simply dummy text of the printing</li>
    <li>Lorem Ipsum is simply dummy text of the printing</li>
  </ul>
  <div class="abs acc" style="top:1589px">Ingredients<svg width="15" height="15" viewBox="0 0 15 15"><path d="M7.5 0V15M0 7.5H15" stroke="#333" stroke-width="1.3"/></svg></div>
  <div class="abs acc" style="top:1639px">Recommended Use<svg width="15" height="15" viewBox="0 0 15 15"><path d="M7.5 0V15M0 7.5H15" stroke="#333" stroke-width="1.3"/></svg></div>
  <div class="abs acc" style="top:1689px">Reviews<svg width="15" height="15" viewBox="0 0 15 15"><path d="M7.5 0V15M0 7.5H15" stroke="#333" stroke-width="1.3"/></svg></div>
  <div class="abs acc" style="top:1740px">Facts<svg width="15" height="15" viewBox="0 0 15 15"><path d="M7.5 0V15M0 7.5H15" stroke="#333" stroke-width="1.3"/></svg></div>
</section>

<footer>
  <div class="abs footer"></div>
  <div class="abs brand footer-brand"><span class="mark"></span>SOLVIA</div>
  <div class="abs social footer-social"><span aria-label="Social link"></span><span aria-label="Social link"></span><span aria-label="Social link"></span></div>
  <nav class="abs footer-nav">
    <a style="left:351px">Home</a>
    <a style="left:451px">About Us</a>
    <a style="left:570px">Blog</a>
    <a style="left:661px">Products</a>
    <a style="left:781px">Contact Us</a>
  </nav>
  <p class="abs copyright">All Right Reserved : Solvia</p>
</footer>

</body>
</html>
```